marketing material folder

I need a folder design that has to inside pockets for distribution of business information and marketing materials

Target Market(s)

Limbcraft Partners referral sources such as physicians, physical therapy clinics and hospitals

Industry/Entity Type

Business

Requirements
Must have
• Similar but not exact design as my brochure project. Must have two pockets on the inside. Must have business card Holder on one of the pockets .
• Addresses and phone numbers for all locations from brochure on the back of folder

```html
<!DOCTYPE html>
<html lang="en">
<head>
<meta charset="utf-8">
<title>Limbcraft Partners – Marketing Folder</title>
<link href="https://fonts.googleapis.com/css2?family=Montserrat:wght@400;600;700&display=swap" rel="stylesheet">
<style>
  :root {
    --backdrop: #e4e4e4;
    --charcoal: #2b2b2c;
    --charcoal-deep: #1c1c1d;
    --steel: #8f9194;
    --silver: #c9cacc;
    --brand-red: #d52b3c;
    --brand-red-deep: #a81c2b;
    --paper-white: #ffffff;
    --muted-white: #d9d9d9;
  }
  * { box-sizing: border-box; margin: 0; padding: 0; }
  html, body { width: 1200px; height: 773px; overflow: hidden; }
  body {
    background: var(--backdrop);
    font-family: "Montserrat", sans-serif;
    position: relative;
  }
  .folder-spread {
    position: absolute;
    left: 110px; top: 60px;
    width: 980px; height: 653px;
    display: flex;
  }
  .folder-back, .folder-front {
    position: relative;
    width: 490px; height: 653px;
    overflow: hidden;
  }
  .back-photo {
    position: absolute; inset: 0;
    background: linear-gradient(160deg, #3a3a3b 0%, var(--charcoal) 45%, var(--charcoal-deep) 100%);
  }
  .back-wave {
    position: absolute; inset: 0;
    width: 490px; height: 653px;
  }
  .office-locations {
    position: absolute;
    left: 248px; top: 262px;
    width: 150px;
    color: var(--paper-white);
  }
  .office-locations h2 {
    font-size: 10px; font-weight: 700;
    margin-bottom: 8px;
  }
  .location {
    display: flex; gap: 6px;
    margin-bottom: 9px;
  }
  .location svg { flex: none; margin-top: 1px; }
  .location p {
    font-size: 7.5px; line-height: 1.35;
    color: var(--muted-white);
  }
  .front-photo {
    position: absolute; inset: 0;
    background: linear-gradient(150deg, #e0505f 0%, var(--brand-red) 40%, #c42333 75%, var(--brand-red-deep) 100%);
  }
  .brand-lockup {
    position: absolute;
    right: 40px; bottom: 72px;
    display: flex; align-items: center; gap: 10px;
  }
  .brand-mark {
    width: 18px; height: 18px; border-radius: 50%;
    background: var(--paper-white);
  }
  .brand-name {
    font-size: 24px; font-weight: 600;
    color: var(--paper-white);
    letter-spacing: 0.2px;
  }
</style>
</head>
<body>
  <main class="folder-spread">
    <section class="folder-back">
      <div class="back-photo" role="img" aria-label="Black and white photo of a young athlete with a running prosthesis sprinting on a track"></div>
      <svg class="back-wave" viewBox="0 0 490 653" aria-hidden="true">
        <path d="M392 0 C330 150 470 300 420 450 C392 540 384 600 402 653 L490 653 L490 0 Z" fill="var(--steel)"/>
        <path d="M410 0 C348 150 488 300 438 450 C410 540 402 600 420 653 L490 653 L490 0 Z" fill="var(--silver)"/>
        <path d="M440 0 C378 150 500 300 462 450 C440 540 432 600 448 653 L490 653 L490 0 Z" fill="var(--brand-red-deep)"/>
      </svg>
      <div class="office-locations">
        <h2>Office Locations:</h2>
        <div class="location">
          <svg width="8" height="10" viewBox="0 0 8 10"><path d="M4 9.5 C1.5 6.5 0.5 5 0.5 3.5 A3.5 3.5 0 0 1 7.5 3.5 C7.5 5 6.5 6.5 4 9.5 Z" fill="none" stroke="#fff" stroke-width="0.9"/><circle cx="4" cy="3.5" r="1.2" fill="none" stroke="#fff" stroke-width="0.8"/></svg>
          <p>4820 Birchwood Avenue,<br>Ste 210 Memphis, TN 38117<br>(901) 555 - 0142<br>(901) 555 - 0178</p>
        </div>
        <div class="location">
          <svg width="8" height="10" viewBox="0 0 8 10"><path d="M4 9.5 C1.5 6.5 0.5 5 0.5 3.5 A3.5 3.5 0 0 1 7.5 3.5 C7.5 5 6.5 6.5 4 9.5 Z" fill="none" stroke="#fff" stroke-width="0.9"/><circle cx="4" cy="3.5" r="1.2" fill="none" stroke="#fff" stroke-width="0.8"/></svg>
          <p>9260 Cedar Ridge Lane,<br>Ste B Houston, TX 77084<br>(281) 555 - 0193<br>(281) 555 - 0127</p>
        </div>
        <div class="location">
          <svg width="8" height="10" viewBox="0 0 8 10"><path d="M4 9.5 C1.5 6.5 0.5 5 0.5 3.5 A3.5 3.5 0 0 1 7.5 3.5 C7.5 5 6.5 6.5 4 9.5 Z" fill="none" stroke="#fff" stroke-width="0.9"/><circle cx="4" cy="3.5" r="1.2" fill="none" stroke="#fff" stroke-width="0.8"/></svg>
          <p>2740 Harmon Road,<br>Ste 300 Arlington, TX 76016<br>(682) 555 - 0164<br>(682) 555 - 0189</p>
        </div>
      </div>
    </section>
    <section class="folder-front">
      <div class="front-photo" role="img" aria-label="Red-toned photo of a runner with a prosthetic leg leaping across rocky hills"></div>
      <div class="brand-lockup">
        <span class="brand-mark"></span>
        <span class="brand-name">Limbcraft Partners</span>
      </div>
    </section>
  </main>
</body>
</html>
```